Birthday Party Invitation for Jasper's 18th Birthday Party

Our eldest son Jasper is turning 18 and we are having a party at home to celebrate the occasion. This project is about creating an invitation that will go to our friends and family. We like things to be nicely designed so posting it to pixel harbor seemed to be the way to go.
The invitation needs to be able to be printed onto an A4 piece of paper. We have access to a color copier so it can be nice and bright.

We want an invitation that conveys a sense of occasion and looks as though we have put time and effort into having a great night to celebrate his 18th.
I have included some photo's of Jasper. They can go onto the invitation as is or they can be given some treatment to form a theme when on the invitiation. I'll leave the treatment of the photo's to the individual designer.

Target Market(s)

Friends and Family

Font styles to use
Sans Serif

Colors

Designer to choose colors to be used in the design.

Requirements
Must have
• The invitation must have the time, date and location of the party.
• Details:
• Saturday 29th of July 2017 7.00pm
• 41 Brackmere Lane, Fenwood
• Food and Drinks provided It must be bright and colourful and convey a sense of excitement.
Nice to have
• Inclusion of the photo's that I have uploaded.
Should not have
• any boring bits

```html
<!DOCTYPE html>
<html lang="en">
<head>
<meta charset="utf-8">
<title>Jasper is Turning 18 – Birthday Invitation</title>
<link rel="stylesheet" href="https://fonts.googleapis.com/css2?family=Pacifico&family=Lobster+Two:ital,wght@1,700&family=Josefin+Sans:wght@600;700&display=swap">
<style>
  :root {
    --backdrop: #dccfb6;
    --night: #0d1a3c;
    --night-mid: #1c3463;
    --night-glow: #2b4a86;
    --teal-light: #5bb6cf;
    --ring: #215f78;
    --ink: #0b1426;
    --white: #ffffff;
    --paper-white: #f1f1f1;
  }
  * { box-sizing: border-box; margin: 0; padding: 0; }
  html, body { width: 1200px; height: 1000px; overflow: hidden; }
  body { background: var(--backdrop); position: relative; }

  .invitation {
    position: absolute; left: 275px; top: 40px;
    width: 650px; height: 920px; overflow: hidden;
    background: radial-gradient(ellipse at 70% 20%, var(--night-glow) 0%, var(--night-mid) 35%, var(--night) 75%);
    box-shadow: 0 10px 30px rgba(0,0,0,.18);
  }

  .hero-photo {
    position: absolute; left: 40px; top: 110px; width: 380px; height: 520px;
    border-radius: 190px 190px 40px 40px;
    background: radial-gradient(ellipse at 50% 32%, #e9b98f 0%, #c98d62 28%, #8a5c44 46%, #2a2e48 72%, rgba(26,34,64,0) 100%);
  }

  .lower-band { position: absolute; left: 0; top: 0; width: 650px; height: 920px; }

  .centered {
    position: absolute; white-space: nowrap; text-align: center;
    transform: translate(-50%, -50%) rotate(var(--tilt));
  }

  .headline-name {
    left: 465px; top: 150px; --tilt: -20deg;
    font-family: "Pacifico", cursive; font-weight: 400; font-size: 100px; line-height: 1.3;
    color: var(--white); text-shadow: 3px 4px 0 rgba(0,0,0,.25);
  }
  .headline-turning {
    left: 490px; top: 262px; --tilt: -20deg;
    font-family: "Josefin Sans", sans-serif; font-weight: 700; font-size: 34px; line-height: 1;
    color: var(--white); letter-spacing: 1px;
  }
  .headline-age {
    left: 515px; top: 385px; --tilt: -8deg;
    font-family: "Josefin Sans", sans-serif; font-weight: 700; font-size: 190px; line-height: 1;
    color: var(--paper-white); text-shadow: 4px 5px 0 rgba(0,0,0,.25);
  }

  .memory-photo {
    position: absolute; width: 160px; height: 160px; border-radius: 50%;
    border: 11px solid var(--ring);
    box-shadow: 0 0 0 4px var(--teal-light);
  }
  .memory-photo--pool { left: 20px; top: 540px; background: radial-gradient(circle at 55% 35%, #e2c89a, #4fb4d6 55%, #2e8fb8); }
  .memory-photo--sister { left: 175px; top: 570px; background: radial-gradient(circle at 50% 40%, #e0b896, #6b8a4a 60%, #3f5a2c); }
  .memory-photo--family { left: 330px; top: 540px; background: radial-gradient(circle at 50% 45%, #d9ad8c, #3b4a6a 55%, #2c3e2a); }
  .memory-photo--school { left: 475px; top: 480px; background: radial-gradient(circle at 50% 40%, #d8ac88, #6a2a3a 50%, #8fb3c9); }

  .celebrate {
    left: 330px; top: 762px; --tilt: -15deg; width: 560px;
    color: var(--ink); font-family: "Lobster Two", cursive; font-style: italic; font-weight: 700;
  }
  .celebrate-title { font-size: 44px; line-height: 1.1; }
  .celebrate-sub { font-size: 23px; line-height: 1.4; padding-left: 40px; }

  .party-details {
    left: 420px; top: 890px; --tilt: -15deg; width: 460px; height: 200px;
    background: var(--ink); color: var(--white);
    font-family: "Josefin Sans", sans-serif; font-weight: 700; font-size: 20px; line-height: 1.3;
    padding-top: 14px; text-transform: uppercase;
  }
</style>
</head>
<body>
  <main class="invitation">
    <div class="hero-photo" role="img" aria-label="Portrait photo of Jasper smiling, wearing a dark knit jumper"></div>

    <svg class="lower-band" viewBox="0 0 650 920" aria-hidden="true">
      <defs>
        <linearGradient id="tealFade" x1="0" y1="0" x2="0" y2="1">
          <stop offset="0" stop-color="#4aaac6"/>
          <stop offset="1" stop-color="#3591b0"/>
        </linearGradient>
      </defs>
      <path d="M0,640 Q300,740 650,540 L650,920 L0,920 Z" fill="url(#tealFade)"/>
      <path d="M0,880 Q60,870 140,872 L140,920 L0,920 Z" fill="#1d6580"/>
      <path d="M560,840 Q610,810 650,790 L650,920 L560,920 Z" fill="#1d6580"/>
    </svg>

    <h1 class="centered headline-name">Jasper</h1>
    <p class="centered headline-turning">IS TURNING</p>
    <p class="centered headline-age">18</p>

    <div class="memory-photo memory-photo--pool" role="img" aria-label="Photo of Jasper playing water polo in the pool"></div>
    <div class="memory-photo memory-photo--sister" role="img" aria-label="Photo of Jasper with his sister in the garden"></div>
    <div class="memory-photo memory-photo--family" role="img" aria-label="Photo of Jasper in a tuxedo with his parents"></div>
    <div class="memory-photo memory-photo--school" role="img" aria-label="Photo of Jasper in his school blazer by a river"></div>

    <div class="centered celebrate">
      <p class="celebrate-title">Let’s Celebrate his Birthday</p>
      <p class="celebrate-sub">and have lots of food and drinks!</p>
    </div>

    <div class="centered party-details">
      <p>Saturday | July 29, 2017 | 7.00pm</p>
      <p>41 Brackmere Lane,</p>
      <p>Fenwood</p>
    </div>
  </main>
</body>
</html>
```